Brochure design for 3D ultrasound company

I am looking for a clean and modern and edgy brochure for my ultrasound company. We are a fairly new company specialize in 3D/4D ultrasounds.Our brochures will be placed in OB-GYN offices in high end areas around Los Angeles, so we need something that will stand out and capture a modern woman's attention. Our logo is currently in the process of being designed, so I don't have a picture to provide quite yet, however it will be our company name"Kite + Lantern" written in a special font that looks like neon lights. I will attach a few images of what our logo will be like, and some initial content that can help provide the layout we would like for the brochure. please feel free to also take a look at our website. www.kitelanternscan.example.

Target Market(s)

Upscale trendy women.

Colors
eea4c8
33a6d7
fee18a

Requirements
Should not have
• too many colors.

```html
<!DOCTYPE html>
<html lang="en">
<head>
<meta charset="utf-8">
<title>Kite + Lantern — Mobile 3D/4D Ultrasound Brochure</title>
<link rel="stylesheet" href="https://fonts.googleapis.com/css2?family=Open+Sans:wght@400;600;700;800&family=Source+Sans+3:wght@400;600&family=Montserrat:wght@500;700&display=swap">
<style>
  :root {
    --pink: #f06bbd;
    --pink-soft: #f7b6dc;
    --pink-pale: #fbe3f1;
    --plum: #6b2f63;
    --plum-deep: #3a1838;
    --ink: #111111;
    --white: #ffffff;
    --blue: #5f7fcf;
  }
  * { margin: 0; padding: 0; box-sizing: border-box; }
  html, body { width: 1200px; height: 927px; overflow: hidden; background: var(--white); }
  .brochure { position: relative; width: 1200px; height: 927px; display: flex; }
  .panel { position: relative; width: 400px; height: 927px; overflow: hidden; }

  /* Left panel */
  .panel--guide {
    background: linear-gradient(90deg, var(--pink-soft) 0%, #fde9f4 45%, var(--white) 100%);
  }
  .photo { position: absolute; left: 0; width: 400px; }
  .photo--newborn-top { top: 0; height: 162px; background: linear-gradient(135deg, #e9cfcf 0%, #d7b6c4 55%, #a472b5 100%); }
  .photo--newborn-bottom { top: 171px; height: 195px; background: linear-gradient(135deg, #f1e6e6 0%, #d9b7d6 50%, #b884c7 80%, #3f8a6c 100%); }
  .guide-title {
    position: absolute; left: 16px; top: 318px;
    font: 800 46px/1 "Open Sans", sans-serif; color: var(--ink); letter-spacing: -1px;
  }
  .guide-list { position: absolute; left: 15px; top: 385px; width: 385px; }
  .guide-item {
    font: 400 16.5px/24.5px "Open Sans", sans-serif; color: var(--ink); margin-bottom: 24px;
  }
  .guide-item b { font-weight: 700; }

  /* Middle panel */
  .panel--about {
    background: linear-gradient(180deg, var(--pink-soft) 0%, var(--pink-pale) 18%, var(--white) 45%, var(--white) 62%, var(--pink-pale) 82%, var(--pink-soft) 100%);
    text-align: center;
  }
  .about-title {
    position: absolute; left: 0; width: 400px; top: 58px;
    font: 600 33px/35px "Source Sans 3", sans-serif; color: var(--pink); letter-spacing: -1.5px;
  }
  .about-body {
    position: absolute; left: 8px; width: 384px; top: 196px;
    font: 400 21px/30.5px "Source Sans 3", sans-serif; color: var(--ink); letter-spacing: -0.3px;
  }
  .about-name {
    position: absolute; left: 0; width: 400px; top: 530px;
    font: 700 28px/1 "Montserrat", sans-serif; color: var(--pink); letter-spacing: 6px;
  }
  .contact-list { position: absolute; left: 0; width: 400px; top: 684px; list-style: none; }
  .contact-list li {
    font: 400 19px/1 "Source Sans 3", sans-serif; color: var(--ink); height: 45.5px;
  }
  .contact-list b { font: 700 20px/1 "Open Sans", sans-serif; }

  /* Right panel */
  .panel--cover { background: var(--plum-deep); }
  .photo--belly {
    position: absolute; inset: 0;
    background:
      radial-gradient(ellipse 260px 330px at 330px 520px, #b89a9a 0%, #8c6b70 45%, transparent 75%),
      linear-gradient(180deg, #7d3f74 0%, #5a2b56 40%, #2e1a2a 100%);
  }
  .shape { position: absolute; inset: 0; }
  .cover-tagline {
    position: absolute; left: 21px; top: 30px;
    font: 700 25px/40px "Montserrat", sans-serif; color: var(--white); letter-spacing: 7px;
  }
  .cover-name {
    position: absolute; left: 0; width: 400px; text-align: center;
    font: 800 58px/1 "Open Sans", sans-serif; color: var(--ink);
  }
  .cover-name--first { top: 300px; letter-spacing: 26px; padding-left: 26px; }
  .cover-name--plus { top: 372px; font-size: 60px; }
  .cover-name--second { top: 446px; font-size: 52px; letter-spacing: 8px; padding-left: 8px; }
  .cover-promise {
    position: absolute; right: 8px; top: 660px; text-align: right;
    font: 700 24px/38px "Montserrat", sans-serif; color: var(--white); letter-spacing: 8px;
  }
  .call-band {
    position: absolute; left: 140px; top: 802px; width: 260px; height: 50px;
    background: linear-gradient(90deg, var(--blue) 0%, #b47fd4 60%, #e58bd0 100%);
  }
  .call-text {
    position: absolute; left: 181px; top: 800px;
    font: 800 24px/28px "Open Sans", sans-serif; color: var(--white);
  }
</style>
</head>
<body>
<main class="brochure">

  <section class="panel panel--guide">
    <div class="photo photo--newborn-top" role="img" aria-label="Photo of a sleeping newborn in a knitted flower cap"></div>
    <div class="photo photo--newborn-bottom" role="img" aria-label="Photo of a sleeping newborn wearing a purple knitted rosebud hat"></div>
    <h2 class="guide-title">WHAT'S WHAT...</h2>
    <div class="guide-list">
      <p class="guide-item"><b>2D</b> is the traditional black and white photo—<br>you know, the one that<br>you want to get emotional about, but you don't<br>know what you're looking at.</p>
      <p class="guide-item"><b>3D</b> is an image of the fetus and it's features. So<br>you can see the baby has dad's nose, and mom's<br>lips.</p>
      <p class="guide-item"><b>4D</b> is 3D, but with motion. You can see the baby<br>yawn, move it's arm, or even<br>give you a smile.</p>
      <p class="guide-item"><b>HD</b> is also 3D, but better.<br>Now you can see a rendering of the baby's skin<br>making<br>it the most realistic fetal image possible..we are<br>one of the few in Los<br>Angeles that have the newest HD capable<br>machines</p>
    </div>
  </section>

  <section class="panel panel--about">
    <h2 class="about-title">Kite + Lantern is a mobile<br>3D ultrasound company</h2>
    <p class="about-body">servicing Los Angeles, and surrounding areas.&nbsp; We take great pride in being one of LA's first mobile Ultrasound companies and for being an all female business! Our mission is to provide an unforgettable experience for expectant mothers in the comfort of their home!</p>
    <p class="about-name">KITE+LANTERN</p>
    <ul class="contact-list">
      <li><b>Telephone</b> : (555) 240-1187</li>
      <li>www.kitelanternscan.example</li>
      <li><b>Email</b> : info@kitelanternscan.example</li>
      <li><b>Instagram</b>: kite_lantern</li>
      <li><b>Facebook</b> : @kitelanternscan</li>
    </ul>
  </section>

  <section class="panel panel--cover">
    <div class="photo--belly" role="img" aria-label="Photo of a pregnant woman's bare belly cradled by her hands"></div>
    <svg class="shape" width="400" height="927" viewBox="0 0 400 927" aria-hidden="true">
      <polygon points="0,0 400,0 400,30 110,215 0,195" fill="#8a3f86" opacity="0.55"/>
      <polygon points="230,0 400,0 400,25 290,140" fill="#e9c8f0" opacity="0.7"/>
      <polygon points="0,195 110,215 0,300" fill="#5a2458" opacity="0.5"/>
      <polygon points="400,605 260,606 30,700 0,927 400,927" fill="#e58bd0" opacity="0.75"/>
      <polygon points="30,700 260,730 0,910" fill="#7d2f78" opacity="0.55"/>
    </svg>
    <p class="cover-tagline">A mobile 3D/4D<br>ultrasound<br>service</p>
    <p class="cover-name cover-name--first">KITE</p>
    <p class="cover-name cover-name--plus">+</p>
    <p class="cover-name cover-name--second">LANTERN</p>
    <p class="cover-promise">Ultrasound<br>in the comfort<br>of your home</p>
    <div class="call-band"></div>
    <p class="call-text">CALL TODAY!<br>555-240-1187</p>
  </section>

</main>
</body>
</html>
```